Hi, We are global cloud printer looking to start a ad print run, we require full and half page print ad's designed with the following dimensions

Full page dimensions:

Image area: 345 mm in height x 260 mm (6 columns) in width
Trim area: 368 mm in height x 280 mm (6 columns) in width
Bleed area: 371 mm in height x 283 mm (6 columns) in width

Half-page dimensions:
270 mm in height x 172 mm (4 columns) in width

We want a minimalistic ad that really stands out from the crowd, with a full page we want it to make an impact and drive people towards our site.

The site is www.plaventro.com , we would like to match the look and feel but would like the wow factor so our open to all concepts.

We would like the following tagline incorporated in the Ad The cloud you've been waiting for, might be closer than you think.

```html
<!DOCTYPE html>
<html lang="en">
<head>
<meta charset="utf-8">
<title>Plaventro Cloud – Full Page Ad</title>
<link rel="stylesheet" href="https://fonts.googleapis.com/css2?family=Roboto:ital,wght@1,100&family=Roboto+Condensed:ital,wght@1,800&family=Open+Sans:wght@700&display=swap">
<style>
  :root {
    --sky-light: #2489cc;
    --sky-mid: #1f73b8;
    --sky-deep: #1f5194;
    --cloud-tint: rgba(140, 180, 230, 0.22);
    --type-white: #ffffff;
    --accent-green: #9ccb3b;
    --url-ink: #0d0d12;
  }
  html, body {
    margin: 0;
    padding: 0;
    overflow: hidden;
    background: #ffffff;
  }
  .ad {
    position: relative;
    width: 914px;
    height: 1200px;
    overflow: hidden;
    background: linear-gradient(200deg, var(--sky-light) 0%, var(--sky-mid) 50%, var(--sky-deep) 100%);
  }
  .cloud-art {
    position: absolute;
    left: 36px;
    top: 128px;
    width: 776px;
    height: 522px;
    background:
      radial-gradient(ellipse 16% 14% at 15% 12%, var(--cloud-tint), transparent 100%),
      radial-gradient(ellipse 50% 42% at 58% 62%, var(--cloud-tint), transparent 100%);
  }
  .tagline {
    margin: 0;
    font-weight: normal;
  }
  .tagline-line {
    position: absolute;
    right: 54px;
    white-space: nowrap;
    line-height: 1;
    color: var(--type-white);
    font-family: "Roboto", sans-serif;
    font-style: italic;
    font-weight: 100;
    font-size: 96px;
    letter-spacing: -1px;
  }
  .tagline-line--first { top: 74px; font-size: 116px; letter-spacing: 0; }
  .tagline-line--2 { top: 180px; letter-spacing: 2.5px; }
  .tagline-line--3 { top: 266px; }
  .tagline-line--4 { top: 361px; letter-spacing: 0; }
  .tagline-line--5 { top: 463px; }
  .tagline-line--last { top: 575px; right: 48px; font-size: 118px; }
  .highlight {
    font-family: "Roboto Condensed", sans-serif;
    font-weight: 800;
    font-style: italic;
    color: var(--accent-green);
    letter-spacing: 0;
  }
  .highlight-stop {
    font-size: 30px;
  }
  .site-url {
    position: absolute;
    left: 0;
    right: 0;
    top: 1130px;
    margin: 0;
    text-align: center;
    font-family: "Open Sans", sans-serif;
    font-weight: 700;
    font-size: 41px;
    line-height: 1;
    color: var(--url-ink);
  }
</style>
</head>
<body>
  <main class="ad">
    <div class="cloud-art" role="img" aria-label="Light outline drawing of a small cloud and a large cloud behind the tagline"></div>

    <h1 class="tagline">
      <span class="tagline-line tagline-line--first">The <span class="highlight">cloud</span></span>
      <span class="tagline-line tagline-line--2">you’ve been</span>
      <span class="tagline-line tagline-line--3">waiting for,</span>
      <span class="tagline-line tagline-line--4">might be</span>
      <span class="tagline-line tagline-line--5">closer than you</span>
      <span class="tagline-line tagline-line--last"><span class="highlight">think<span class="highlight-stop">.</span></span></span>
    </h1>

    <p class="site-url">www.plaventro.com</p>
  </main>
</body>
</html>
```